PowerPoint/Keynote Design Project - Corvanel

I need a fairly straightforward design for a presentation I currently use in Keynote. It is very basic, as I developed it in an Excel spreadsheet and a friend helped migrate it over to Keynote.
I don't want it to be overly complex and I don't want it to be too busy. It should not contain too many distracting elements, but I think it needs some professional design changes to make it more appealing to the eye. I think colors should be soft and not flashy; transitions should be simple.
==================================
In response to several questions received, I have added two files. One file is the actual presentation I currently use. I run it in Keynote but I uploaded it in Powerpoint. As you can see, it is a single page but it is developed sequentially.
The other file (Examples) is just a random selection of slides I chose from several unrelated presentations I use. I am providing this to illustrate the range of colors, type styles, and combinations I frequently use. However, this isn't meant to limit the choice of colors you might recommend. I am open to any colors which might enhance the overall effect of the presentation without overpowering its message.
Thank you for all the comments and questions I have received thus far.

```html
<!DOCTYPE html>
<html lang="en">
<head>
<meta charset="utf-8">
<title>Freedom from the Power of Sin</title>
<link rel="stylesheet" href="https://fonts.googleapis.com/css2?family=Lato:wght@700;900&display=swap">
<style>
  :root {
    --sky-deep: #16539c;
    --sky-mid: #4f8fd0;
    --sky-light: #b9d6f0;
    --haze: #ffffff;
    --title-orange-top: #ffd08a;
    --title-orange-bottom: #f08a1c;
    --heading-red: #d8291c;
    --stage-ink: #141414;
    --box-top: #fbb25c;
    --box-bottom: #e9741a;
    --box-edge: #d96a12;
    --arrow-blue: #4a78b8;
    --arrow-edge: #2f5a95;
    --cloud-edge: #3a3a3a;
    --footer-red: #b01e1e;
  }
  html, body {
    margin: 0;
    padding: 0;
    overflow: hidden;
    background: #ffffff;
  }
  .slide {
    position: relative;
    width: 1200px;
    height: 895px;
    overflow: hidden;
    font-family: "Lato", Arial, sans-serif;
  }
  .backdrop {
    position: absolute;
    inset: 0;
    background:
      linear-gradient(90deg, transparent 47%, rgba(255,255,255,0.55) 50%, transparent 53%),
      radial-gradient(circle at 50% 24%, rgba(255,255,255,0.95) 0, rgba(220,235,255,0.5) 60px, transparent 180px),
      linear-gradient(180deg, var(--sky-deep) 0%, var(--sky-mid) 28%, var(--sky-light) 46%, var(--haze) 62%, var(--haze) 100%);
  }
  .title {
    position: absolute;
    top: 10px;
    left: 0;
    width: 100%;
    margin: 0;
    text-align: center;
    font-size: 52px;
    font-weight: 900;
    background: linear-gradient(180deg, var(--title-orange-top), var(--title-orange-bottom));
    -webkit-background-clip: text;
    background-clip: text;
    color: transparent;
    filter: drop-shadow(0 0 4px rgba(255,255,255,0.8));
  }
  .freedom {
    position: absolute;
    margin: 0;
    width: 300px;
    text-align: center;
    font-size: 30px;
    line-height: 1.27;
    font-weight: 700;
    color: var(--heading-red);
    text-shadow: 0 0 4px #fff, 0 0 8px rgba(255,255,255,0.8);
  }
  .freedom--penalty { left: 93px; top: 148px; }
  .freedom--presence { left: 803px; top: 148px; }
  .stage {
    position: absolute;
    margin: 0;
    font-weight: 900;
    color: var(--stage-ink);
    text-shadow: 2px 2px 3px rgba(0,0,0,0.35);
    line-height: 1;
  }
  .stage .reflection {
    display: block;
    transform: scaleY(-1);
    opacity: 0.3;
    text-shadow: none;
    filter: blur(0.6px);
    -webkit-mask-image: linear-gradient(0deg, #000, transparent 90%);
    mask-image: linear-gradient(0deg, #000, transparent 90%);
  }
  .stage--justification { left: 98px; top: 372px; font-size: 37px; }
  .stage--glorification { left: 834px; top: 368px; font-size: 37px; }
  .stage--sanctification { left: 420px; top: 468px; font-size: 43px; }
  .flow {
    position: absolute;
    inset: 0;
  }
  .cloud-label {
    position: absolute;
    text-align: center;
    font-size: 22px;
    font-weight: 700;
    line-height: 1.2;
    color: var(--stage-ink);
    font-family: Arial, Helvetica, sans-serif;
  }
  .cloud-label--birth { left: 140px; top: 506px; width: 150px; }
  .cloud-label--death { left: 18px; top: 654px; width: 140px; }
  .step {
    position: absolute;
    display: flex;
    align-items: center;
    justify-content: center;
    text-align: center;
    box-sizing: border-box;
    background: linear-gradient(180deg, var(--box-top), var(--box-bottom));
    border: 1px solid var(--box-edge);
    box-shadow: 3px 4px 6px rgba(0,0,0,0.35);
    color: #ffffff;
    font-weight: 900;
    text-shadow: 1px 1px 2px rgba(0,0,0,0.45);
    padding: 6px 12px;
  }
  .step--birth { left: 83px; top: 758px; width: 240px; height: 73px; font-size: 27px; }
  .step--death { left: 860px; top: 531px; width: 238px; height: 73px; font-size: 27px; }
  .step--process { left: 346px; top: 614px; width: 504px; height: 129px; font-size: 27px; line-height: 1.3; }
  .footer-note {
    position: absolute;
    right: 12px;
    bottom: 8px;
    margin: 0;
    font-size: 27px;
    font-weight: 700;
    color: var(--footer-red);
  }
</style>
</head>
<body>
<main class="slide">
  <div class="backdrop" role="img" aria-label="Blue sky with clouds fading to white, a glowing cross standing at the centre"></div>

  <h1 class="title">Freedom from the Power of Sin</h1>

  <p class="freedom freedom--penalty">Freedom from the Penalty for Sin</p>
  <p class="freedom freedom--presence">Freedom from the Presence of Sin</p>

  <h2 class="stage stage--justification">Justification<span class="reflection" aria-hidden="true">Justification</span></h2>
  <h2 class="stage stage--glorification">Glorification<span class="reflection" aria-hidden="true">Glorification</span></h2>
  <h2 class="stage stage--sanctification">Sanctification<span class="reflection" aria-hidden="true">Sanctification</span></h2>

  <svg class="flow" width="1200" height="895" viewBox="0 0 1200 895" aria-hidden="true">
    <g fill="#ffffff" stroke="var(--cloud-edge)" stroke-width="1.5">
      <path class="cloud" d="M150 560 C128 560 126 536 146 532 C140 512 166 500 182 512 C190 494 220 492 232 508 C248 494 278 502 276 522 C298 524 300 552 280 556 C286 574 258 582 246 570 C234 584 204 584 196 570 C182 582 156 578 150 560 Z"/>
      <path class="cloud" d="M28 698 C8 698 6 674 24 670 C18 650 44 638 60 650 C68 632 98 630 108 646 C124 634 152 642 150 660 C170 662 172 690 154 694 C158 712 132 718 122 706 C110 720 82 720 74 706 C60 718 34 714 28 698 Z"/>
    </g>
    <g fill="var(--arrow-blue)" stroke="var(--arrow-edge)" stroke-width="1.5">
      <line x1="299" y1="488" x2="299" y2="730" stroke="var(--arrow-edge)" stroke-width="3"/>
      <line x1="299" y1="667" x2="246" y2="667" stroke="var(--arrow-edge)" stroke-width="3"/>
      <polygon points="299,466 284,490 314,490"/>
      <polygon points="299,752 284,728 314,728"/>
      <polygon points="226,667 250,654 250,680"/>
    </g>
    <path class="ridge" d="M751 804 L790 786 L818 790 L850 772 L880 776 L905 760 L935 764 L960 748 L990 752 L1015 738 L1045 742 L1070 726 L1095 730 L1125 712 L1150 716 L1175 700 L1200 698" fill="none" stroke="#000000" stroke-width="2"/>
  </svg>

  <div class="cloud-label cloud-label--birth">Spiritually<br>Birth</div>
  <div class="cloud-label cloud-label--death">Spiritually<br>Death</div>

  <div class="step step--birth">Physical Birth</div>
  <div class="step step--process">Process of Yielding to the Guidance and Empowerment of the Holy Spirit</div>
  <div class="step step--death">Physical Death</div>

  <p class="footer-note">Submission/Good Works/ Obedience</p>
</main>
</body>
</html>
```